Business Card design for construction company

I would like a business card design for a construction company - Harlow Constructions. I have attached the ai logo file for use. I would like the card to be very smart and clean and incorporate only white and the two colours in the logo. I would like the card to have two sides. One side can just have the logo, the other with the relevant information.

Target Market(s)

Building and Construction Clients

Industry/Entity Type

Business

Contact Information for Business Card

Name: Tom Pardoe
Company: Harlow Constructions Pty Limited
Address: 14 Mallee Crescent Carrow Vale 2093
Phone: 0427 531 068
Email: tomp@harlowbuild-example.com.au

Font styles to use
Serif
Sans Serif

Requirements
Must have
• Details noted above
• Logo as provided
• Colours as in logo
• Square edges
• A font that compliments the logo
Should not have
• Any colour other than white and those in logo
• Rounded edges

```html
<!DOCTYPE html>
<html lang="en">
<head>
<meta charset="utf-8">
<title>Harlow Constructions – Business Card</title>
<link href="https://fonts.googleapis.com/css2?family=Michroma&display=swap" rel="stylesheet">
<style>
  :root {
    --brand-blue: #00acea;
    --brand-grey: #4a4a4c;
    --paper: #ffffff;
    --backdrop: #e9eaec;
    --sketch: rgba(255, 255, 255, 0.28);
  }
  * { box-sizing: border-box; margin: 0; padding: 0; }
  html, body {
    width: 1200px;
    height: 1200px;
    overflow: hidden;
    background: var(--backdrop);
    font-family: "Michroma", sans-serif;
  }
  .canvas {
    position: relative;
    width: 1200px;
    height: 1200px;
  }
  .card {
    position: absolute;
    width: 564px;
    height: 348px;
    overflow: hidden;
    box-shadow: 0 14px 30px rgba(0, 0, 0, 0.18);
  }
  /* Front: contact details */
  .card--front {
    left: 190px;
    top: 230px;
    background: var(--paper);
    color: var(--brand-grey);
  }
  .wordmark {
    position: absolute;
    left: 40px;
    right: 40px;
    top: 66px;
    font-size: 21px;
    line-height: 1;
    letter-spacing: 1px;
    white-space: nowrap;
  }
  .card--front .wordmark { color: var(--brand-grey); }
  .holder-name {
    position: absolute;
    left: 40px;
    top: 168px;
    font-size: 20px;
    letter-spacing: -0.5px;
  }
  .contact-list {
    position: absolute;
    left: 32px;
    top: 262px;
    list-style: none;
    font-size: 13px;
    letter-spacing: -0.2px;
  }
  .contact-list li {
    display: flex;
    align-items: center;
    height: 24px;
    white-space: nowrap;
  }
  .contact-list svg {
    width: 13px;
    height: 13px;
    margin-right: 12px;
    flex: none;
    fill: var(--brand-blue);
  }
  /* Back: brand side */
  .card--back {
    left: 420px;
    top: 660px;
    background: var(--brand-blue);
  }
  .card--back .wordmark {
    color: var(--paper);
    top: 104px;
  }
  .house-sketch {
    position: absolute;
    left: 200px;
    top: 190px;
    width: 250px;
    height: 130px;
    background: radial-gradient(ellipse at center, var(--sketch) 0%, rgba(255,255,255,0.06) 60%, rgba(255,255,255,0) 75%);
  }
</style>
</head>
<body>
<main class="canvas">
  <section class="card card--front" aria-label="Business card front">
    <div class="wordmark">HARLOW CONSTRUCTIONS</div>
    <div class="holder-name">Tom Pardoe</div>
    <ul class="contact-list">
      <li>
        <svg viewBox="0 0 12 12" aria-hidden="true"><path d="M6 0a4 4 0 0 0-4 4c0 3 4 6.5 4 6.5s4-3.5 4-6.5a4 4 0 0 0-4-4zm0 5.6A1.6 1.6 0 1 1 6 2.4a1.6 1.6 0 0 1 0 3.2zM2 11h8v1H2z"/></svg>
        14 Mallee Crescent Carrow Vale 2093
      </li>
      <li>
        <svg viewBox="0 0 12 12" aria-hidden="true"><path d="M2.4 0.6l2 2.2-1 1.3c.7 1.6 2 2.9 3.6 3.6l1.3-1 2.2 2-1.2 1.9C4.8 10.4 1.2 6.8.8 2z"/></svg>
        0427 531 068
      </li>
      <li>
        <svg viewBox="0 0 12 12" aria-hidden="true"><path d="M0 2h12v8H0zM1 3v.4l5 3.3 5-3.3V3z"/></svg>
        tomp@harlowbuild-example.com.au
      </li>
    </ul>
  </section>

  <section class="card card--back" aria-label="Business card back">
    <div class="wordmark">HARLOW CONSTRUCTIONS</div>
    <div class="house-sketch" role="img" aria-label="Faint white line sketch of a two-storey house"></div>
  </section>
</main>
</body>
</html>
```